the letter head should have the logo ( may be top left), " Fenwick Ridge Institute" (may be top/middle ) and the two clinics info in a vertical column ( along the left side of the page )

Target Market(s)

other physicians and official letters

Requirements
Must have
• the info provided in the attachements

```html
<!DOCTYPE html>
<html lang="en">
<head>
<meta charset="utf-8">
<title>Fenwick Ridge Institute – Letterhead and Envelope</title>
<link rel="stylesheet" href="https://fonts.googleapis.com/css2?family=Cinzel:wght@400;600&family=Tinos:wght@400;700&family=Arimo:wght@400&display=swap">
<style>
  :root{
    --bg:#ececec;
    --paper:#ffffff;
    --paper-edge:#d6d6d8;
    --fade-end:#bdbdc2;
    --brand:#a31a5c;
    --ink:#2f3a46;
    --text:#7a7a7e;
    --detail:#333338;
    --watermark:rgba(255,255,255,0.75);
  }
  *{margin:0;padding:0;box-sizing:border-box}
  html,body{width:1200px;height:1200px;overflow:hidden;background:var(--bg)}
  .stage{position:relative;width:1200px;height:1200px}

  .sheet{position:absolute;border:1px solid var(--paper-edge);overflow:hidden}
  .letterhead{left:115px;top:101px;width:769px;height:995px;
    background:linear-gradient(to bottom,var(--paper) 0%,var(--paper) 58%,var(--fade-end) 100%)}
  .envelope{left:251px;top:465px;width:859px;height:372px;
    background:linear-gradient(to bottom,var(--paper) 0%,var(--paper) 30%,var(--fade-end) 100%)}

  .brand{position:absolute;display:flex;align-items:flex-start;gap:8px}
  .brand-square{width:46px;height:46px;background:var(--brand);margin-top:4px}
  .brand-name{font-family:"Cinzel",serif;font-weight:600;color:var(--ink);
    font-size:17px;line-height:20px;letter-spacing:0.5px}
  .letterhead .brand{left:19px;top:17px}
  .envelope .brand{left:18px;top:15px}

  .office{position:absolute;left:19px;font-family:"Tinos",serif;color:var(--detail);font-size:10.5px;line-height:15px}
  .office-title{color:var(--brand);font-weight:700;font-size:11px;margin-bottom:1px}
  .office-line{display:flex;align-items:center;gap:5px}
  .office-line svg{width:8px;height:8px;fill:var(--brand);flex:none}
  .letterhead .office.first{top:119px}
  .letterhead .office.second{top:196px}
  .envelope .office.first{top:116px}
  .envelope .office.second{top:194px}

  .subject{position:absolute;left:401px;top:330px;font-family:"Arimo",sans-serif;font-size:16px;color:var(--text);
    display:flex;align-items:baseline;gap:6px}
  .subject-rule{width:266px;border-bottom:1.5px dotted var(--text);transform:translateY(-3px)}

  .letter{position:absolute;left:54px;width:660px;font-family:"Arimo",sans-serif;color:var(--text)}
  .salutation{top:356px;font-size:18px}
  .body-copy{font-size:12.5px;line-height:16.6px}
  .p1{top:391px}.p2{top:497px}.p3{top:611px}
  .closing{top:744px;font-size:17px}
  .signer{top:768px;font-size:11px}
  .signature{position:absolute;left:50px;top:808px;width:80px;height:50px;
    background:linear-gradient(135deg,rgba(120,120,126,0.35),rgba(120,120,126,0.08));border-radius:4px}

  .watermark-name{position:absolute;left:0;right:0;text-align:center;font-family:"Cinzel",serif;font-weight:400;
    color:var(--watermark);letter-spacing:1px;white-space:nowrap}
  .letterhead .watermark-name{top:928px;font-size:44px}
  .envelope .watermark-name{top:298px;font-size:44px;text-align:right;padding-right:16px}
</style>
</head>
<body>
<svg width="0" height="0" style="position:absolute" aria-hidden="true">
  <symbol id="icon-phone" viewBox="0 0 10 10"><path d="M2 0.5l2 2-1 1.2c.6 1.3 1.6 2.3 2.9 2.9l1.2-1 2 2-1.3 1.8C4.5 9.2.8 5.5.3 1.8z"/></symbol>
  <symbol id="icon-fax" viewBox="0 0 10 10"><rect x="2.5" y="0.5" width="5" height="3"/><rect x="0.5" y="3.5" width="9" height="4" rx="1"/><rect x="2.5" y="7" width="5" height="2.5"/></symbol>
  <symbol id="icon-pin" viewBox="0 0 10 10"><path d="M5 0.3a3.4 3.4 0 0 0-3.4 3.4C1.6 6.2 5 9.7 5 9.7s3.4-3.5 3.4-6A3.4 3.4 0 0 0 5 .3zm0 4.7a1.3 1.3 0 1 1 0-2.6 1.3 1.3 0 0 1 0 2.6z"/></symbol>
</svg>

<main class="stage">
  <section class="sheet letterhead">
    <div class="brand">
      <div class="brand-square"></div>
      <div class="brand-name">Fenwick<br>Ridge<br>Institute</div>
    </div>

    <div class="office first">
      <div class="office-title">Harlow Office</div>
      <div class="office-line"><svg><use href="#icon-phone"/></svg>555-210-3847</div>
      <div class="office-line"><svg><use href="#icon-fax"/></svg>555-210-3852</div>
      <div class="office-line"><svg><use href="#icon-pin"/></svg>118 N. Alder Ave. Suite 302, 40917</div>
    </div>
    <div class="office second">
      <div class="office-title">Cedar Point Office</div>
      <div class="office-line"><svg><use href="#icon-phone"/></svg>555-384-6021</div>
      <div class="office-line"><svg><use href="#icon-fax"/></svg>555-384-6029</div>
      <div class="office-line"><svg><use href="#icon-pin"/></svg>2745 W. Linden St. Cedar Point 40958</div>
    </div>

    <div class="subject">SUB:<span class="subject-rule"></span></div>

    <p class="letter salutation">Dear Sir</p>
    <p class="letter body-copy p1">Lorem Ipsum is simply dummy text of the printing and typesetting industry. Lorem Ipsum has been the standard dummy text ever since the early days, when a printer took a galley of type and scrambled it to make a type specimen book. It has survived not only five centuries but also the leap into Lorem Ipsum and many versions of Lorem Ipsum.</p>
    <p class="letter body-copy p2">It is a long established fact that a reader will be distracted by the readable content of a page when looking at its layout. The point of using placeholder text is that it has a more even spread of letters, using 'Content here, content here' as opposed to using plain words, making it look like readable English when looking at the page.</p>
    <p class="letter body-copy p3">The point of using sample text is that it reads like 'Content here, content here', and many page layout packages now use it as their default model text. Many versions have evolved over the years, some by accident, some on purpose, like English. Searching for it will uncover many sites still in their infancy.</p>
    <p class="letter closing">Warm regards</p>
    <p class="letter signer">Daniel Reyes M.D.</p>
    <div class="signature" role="img" aria-label="Handwritten signature of the physician"></div>

    <div class="watermark-name">Fenwick Ridge Institute</div>
  </section>

  <section class="sheet envelope">
    <div class="brand">
      <div class="brand-square"></div>
      <div class="brand-name">Fenwick<br>Ridge<br>Institute</div>
    </div>

    <div class="office first">
      <div class="office-title">Harlow Office</div>
      <div class="office-line"><svg><use href="#icon-phone"/></svg>555-210-3847</div>
      <div class="office-line"><svg><use href="#icon-fax"/></svg>555-210-3852</div>
      <div class="office-line"><svg><use href="#icon-pin"/></svg>118 N. Alder Ave. Suite 302, 40917</div>
    </div>
    <div class="office second">
      <div class="office-title">Cedar Point Office</div>
      <div class="office-line"><svg><use href="#icon-phone"/></svg>555-384-6021</div>
      <div class="office-line"><svg><use href="#icon-fax"/></svg>555-384-6029</div>
      <div class="office-line"><svg><use href="#icon-pin"/></svg>2745 W. Linden St. Cedar Point 40958</div>
    </div>

    <div class="watermark-name">Fenwick Ridge Institute</div>
  </section>
</main>
</body>
</html>
```